Tallowreed Advisory Partners Business Card Design

We have the logo we just need someone to design a modern business card design.

Name: Desmond Munkalt
Phone: 3055550148
Mobile: 9175550193
Web:www.tallowreedadvisory.example
email: dmunkalt@tallowreedadvisory.example
Company: Tallowreed Advisory Partners
Title: CEO

Address: 718 Quillmore Ave, Miami, Florida 33190

Target Market(s)

companies over 100 employees

Industry/Entity Type

Business

```html
<!DOCTYPE html>
<html lang="en">
<head>
<meta charset="utf-8">
<title>Tallowreed Advisory Partners Business Card</title>
<link rel="stylesheet" href="https://fonts.googleapis.com/css2?family=Arimo:wght@400;700&display=swap">
<style>
  :root {
    --page: #ffffff;
    --card-top: #1c1d1f;
    --card-bottom: #0c0c0d;
    --card-edge: #2a2b2d;
    --accent: #0b5cff;
    --icon: #1d52e0;
    --white: #ffffff;
    --muted: #8c8c8c;
    --muted-strong: #9a9a9a;
    --divider-dark: #050505;
    --divider-light: #2c2d2f;
  }
  * { margin: 0; padding: 0; box-sizing: border-box; }
  html, body {
    width: 1200px; height: 1000px; overflow: hidden;
    background: var(--page);
    font-family: "Arimo", Arial, sans-serif;
  }
  .canvas { position: relative; width: 1200px; height: 1000px; }

  .card {
    position: absolute; left: 247px; width: 723px; height: 404px;
    border-radius: 28px; overflow: hidden;
    border: 1px solid var(--card-edge);
    background: linear-gradient(160deg, var(--card-top) 0%, #141516 55%, var(--card-bottom) 100%);
  }
  .card--front { top: 37px; }
  .card--back { top: 545px; }

  .card__texture {
    position: absolute; inset: 0;
    background: radial-gradient(ellipse at 50% 40%, rgba(255,255,255,0.06) 0%, rgba(255,255,255,0) 65%);
  }

  /* Front */
  .brand {
    position: absolute; left: 0; right: 0; top: 122px;
    display: flex; flex-direction: column; align-items: center;
    color: var(--white); font-weight: 700; text-align: center;
  }
  .brand__dot {
    width: 102px; height: 102px; border-radius: 50%;
    background: var(--accent); margin-bottom: 18px;
  }
  .brand__name { font-size: 34px; letter-spacing: 1px; line-height: 1; }
  .brand__sub { font-size: 13px; letter-spacing: 0.5px; margin-top: 8px; line-height: 1; }

  /* Back */
  .divider {
    position: absolute; left: 281px; top: 30px; width: 3px; height: 340px;
    background: linear-gradient(90deg, var(--divider-dark) 0 1px, var(--divider-light) 1px 3px);
  }
  .contact {
    position: absolute; right: 469px; text-align: right;
    color: var(--muted); font-size: 14px; line-height: 28px; white-space: nowrap;
  }
  .contact--phones { top: 83px; }
  .contact--address { top: 158px; }
  .contact--web { top: 242px; }
  .contact--email { top: 298px; }

  .icon { position: absolute; left: 300px; width: 46px; height: 46px; }
  .icon svg { width: 100%; height: 100%; fill: none; stroke: var(--icon); stroke-width: 1.6; stroke-linejoin: round; stroke-linecap: round; }
  .icon--phone { top: 82px; }
  .icon--home { top: 158px; }
  .icon--mail { top: 228px; }
  .icon--globe { top: 289px; }

  .person {
    position: absolute; right: 39px; top: 160px; text-align: right; white-space: nowrap;
  }
  .person__name { color: var(--white); font-size: 22px; line-height: 28px; }
  .person__company, .person__title { color: var(--muted-strong); font-size: 20px; line-height: 27px; }
</style>
</head>
<body>
<main class="canvas">

  <section class="card card--front" aria-label="Business card front">
    <div class="card__texture" role="img" aria-label="Dark diagonal pinstripe texture"></div>
    <div class="brand">
      <div class="brand__dot"></div>
      <div class="brand__name">TALLOWREED</div>
      <div class="brand__sub">ADVISORY PARTNERS</div>
    </div>
  </section>

  <section class="card card--back" aria-label="Business card back">
    <div class="card__texture" role="img" aria-label="Dark diagonal pinstripe texture"></div>
    <div class="divider"></div>

    <div class="contact contact--phones">3055550148<br>9175550193</div>
    <div class="contact contact--address">718 Quillmore Ave,<br>Miami, Florida 33190</div>
    <div class="contact contact--web">www.tallowreedadvisory.example</div>
    <div class="contact contact--email">dmunkalt@tallowreedadvisory.example</div>

    <div class="icon icon--phone">
      <svg viewBox="0 0 46 46"><path d="M12 30 C8 26 8 20 12 16 L16 12 L21 17 L17 21 C18 24 22 28 25 29 L29 25 L34 30 L30 34 C26 38 20 38 16 34 Z"/></svg>
    </div>
    <div class="icon icon--home">
      <svg viewBox="0 0 46 46"><path d="M4 22 L23 4 L42 22 M9 18 V42 H37 V18 M19 42 V30 H27 V42"/></svg>
    </div>
    <div class="icon icon--mail">
      <svg viewBox="0 0 46 46"><rect x="6" y="12" width="34" height="22"/><path d="M6 12 L23 26 L40 12 M6 34 L18 22 M40 34 L28 22"/></svg>
    </div>
    <div class="icon icon--globe">
      <svg viewBox="0 0 46 46"><circle cx="23" cy="23" r="15"/><ellipse cx="23" cy="23" rx="6" ry="15"/><path d="M8 23 H38 M11 15 H35 M11 31 H35"/></svg>
    </div>

    <div class="person">
      <div class="person__name">DESMOND MUNKALT</div>
      <div class="person__company">Tallowreed Advisory Partners</div>
      <div class="person__title">CEO</div>
    </div>
  </section>

</main>
</body>
</html>
```